KT Design Business Card

I would like a business card similar to this
https://www.artquorra.com/design/8173920
with my info and a picture of my rifle. You can use something like this
https://www.snaplirra.com/pin/381926405572018843/visual-search/?cropSource=6&h=476&w=268&x=12&y=12
or
https://www.snaplirra.com/pin/219604837751093468/

I have a logo, it is a shepperds staff. I build custom rifles and do Law Enforcement sales. Some where on the card it needs to say something like, "Custom AR's built correctly", "All rifles come with honed uppers and bedded barrels", "All rifles are fully tested and come with a 3 shot card", "Law Enforcement models are available", "Tactical Equipment Consulting", "One stop shop for all tactical equipment"

Business Name: KT Design LLC
Name: Brent Hollis
Phone: (555) 614-2980
Email: brent.ktdesign@mailbriq.com
Address: 3082 Tamblin Ct., Corvane Hill, KX, 29815

Just use the concept of the staff in the attachments the other stuff is not related

```html
<!DOCTYPE html>
<html lang="en">
<head>
<meta charset="UTF-8">
<title>KT Design LLC – Business Card</title>
<link rel="stylesheet" href="https://fonts.googleapis.com/css2?family=Open+Sans:wght@400;600&family=Roboto+Condensed:wght@400&family=Crimson+Text:wght@400&display=swap">
<style>
  :root {
    --backdrop: #e4e4e4;
    --card: #3a3a3a;
    --ink: #ffffff;
    --photo-dark: #2e2e2e;
    --photo-mid: #4a4640;
    --photo-tan: #7d6e58;
  }
  * { margin: 0; padding: 0; box-sizing: border-box; }
  html, body {
    width: 1200px; height: 800px; overflow: hidden;
    background: var(--backdrop);
  }
  .stage { position: relative; width: 1200px; height: 800px; }
  .card {
    position: absolute; width: 490px; height: 280px;
    background: var(--card); color: var(--ink);
    box-shadow: 0 6px 16px rgba(0,0,0,0.25);
    overflow: hidden;
  }
  .card--front { left: 95px; top: 260px; }
  .card--back  { left: 615px; top: 260px; }

  .business-name {
    position: absolute; right: 26px; top: 24px;
    font-family: "Open Sans", sans-serif; font-weight: 600;
    font-size: 22px; line-height: 1.2; color: var(--ink);
  }

  .rifle-photo {
    position: absolute; left: 60px; top: 72px; width: 400px; height: 110px;
    border-radius: 6px;
    background: linear-gradient(100deg, var(--photo-tan) 0%, var(--photo-mid) 30%, var(--photo-dark) 60%, var(--photo-tan) 90%);
    opacity: 0.85;
  }

  .selling-points {
    position: absolute; left: 22px; top: 192px; width: 160px;
    list-style: none; text-align: center;
    font-family: "Crimson Text", serif; font-size: 14px; line-height: 1.15;
  }
  .selling-points li::before { content: "\2022\00a0"; }

  .brand-block {
    position: absolute; left: 20px; top: 140px; width: 170px; text-align: center;
  }
  .brand-block__name {
    font-family: "Open Sans", sans-serif; font-weight: 600;
    font-size: 22px; margin-bottom: 8px;
  }
  .brand-block__spec {
    font-family: "Roboto Condensed", sans-serif; font-size: 15px; line-height: 1.2;
  }

  .contact {
    position: absolute; right: 14px; top: 168px; text-align: right;
    font-family: "Open Sans", sans-serif;
  }
  .contact__name { font-size: 20px; margin-bottom: 6px; margin-right: 20px; }
  .contact__line {
    display: flex; justify-content: flex-end; align-items: center; gap: 6px;
    font-size: 13px; line-height: 22px;
  }
  .contact__icon { width: 12px; height: 12px; flex: none; }
</style>
</head>
<body>
<main class="stage">

  <section class="card card--front">
    <div class="business-name">KT Design LLC</div>
    <div class="rifle-photo" role="img" aria-label="Photograph of a custom AR-style rifle with tan stock, optic sight and magazine"></div>
    <ul class="selling-points">
      <li>One stop shop for all tactical equipment.</li>
      <li>All rifles are fully tested and come with a 3 shot card.</li>
    </ul>
  </section>

  <section class="card card--back">
    <div class="business-name">KT Design LLC</div>

    <div class="brand-block">
      <div class="brand-block__name">KT Design</div>
      <div class="brand-block__spec">KTD 15<br>MULTI CAL<br>S/N: XXXXX</div>
    </div>

    <div class="contact">
      <div class="contact__name">Brent Hollis</div>
      <div class="contact__line">(555) 614-2980
        <svg class="contact__icon" viewBox="0 0 12 12" aria-hidden="true">
          <circle cx="6" cy="6" r="6" fill="#fff"/>
          <path d="M3.5 3.2h1.3l.6 1.5-.8.6a4 4 0 0 0 2 2l.6-.8 1.5.6v1.3c-3 .3-5.5-2.2-5.2-5.2z" fill="#3a3a3a"/>
        </svg>
      </div>
      <div class="contact__line">brent.ktdesign@mailbriq.com
        <svg class="contact__icon" viewBox="0 0 12 12" aria-hidden="true">
          <circle cx="6" cy="6" r="6" fill="#fff"/>
          <rect x="3" y="4" width="6" height="4.2" fill="none" stroke="#3a3a3a" stroke-width="0.9"/>
          <path d="M3 4l3 2.3L9 4" fill="none" stroke="#3a3a3a" stroke-width="0.9"/>
        </svg>
      </div>
      <div class="contact__line">3082 Tamblin Ct., Corvane Hill, KX, 29815
        <svg class="contact__icon" viewBox="0 0 12 12" aria-hidden="true">
          <circle cx="6" cy="6" r="6" fill="#fff"/>
          <path d="M6 2.6a2.2 2.2 0 0 0-2.2 2.2C3.8 6.5 6 9.4 6 9.4s2.2-2.9 2.2-4.6A2.2 2.2 0 0 0 6 2.6z" fill="#3a3a3a"/>
          <circle cx="6" cy="4.8" r="0.8" fill="#fff"/>
        </svg>
      </div>
    </div>
  </section>

</main>
</body>
</html>
```